Business Card Design for a technology company

Our current business card is outdated and stale.

We need a new look and one soon.

We're a telematics (GPS tracking) company based in Australia. Our audiences are transport and logistics company.

Target Market(s)

1. Transport and Logistics Companies
2. Food and Beverage Manufacturers
3. Concrete Businesses

Industry/Entity Type

Logistics

Contact Information for Business Card

Halvor Pinet

Font styles to use
Sans Serif

Colors
3276b5
0255a3
85acd3
cfdeed
ffffff

Requirements
Must have
• Logo
• "Premium Suppliers of Real Time Temperature Tracking"
• Contact Name
• Business Title
• Address
• Telephone
• Mobile
• Email
• Website URL
Nice to have
• Visual representation of tracking or maps.
Should not have
• Image of a satellite as currently shown

```html
<!DOCTYPE html>
<html lang="en">
<head>
<meta charset="utf-8">
<title>Halvor Pinet Business Card</title>
<link rel="stylesheet" href="https://fonts.googleapis.com/css2?family=Questrial&family=Didact+Gothic&family=Roboto:ital,wght@0,500;0,700;1,400;1,700&display=swap">
<style>
  :root {
    --backdrop: #1d1d1f;
    --card-white: #ffffff;
    --brand-blue: #0255a3;
    --brand-mid: #3276b5;
    --brand-light: #85acd3;
    --brand-pale: #cfdeed;
    --ink: #1f1f1f;
    --ink-soft: #555a5f;
    --ink-muted: #6b6f73;
  }
  * { margin: 0; padding: 0; box-sizing: border-box; }
  html, body {
    width: 1200px; height: 960px; overflow: hidden;
    background: var(--backdrop);
  }
  .canvas { position: relative; width: 1200px; height: 960px; }

  .card {
    position: absolute; width: 600px; height: 342px;
    box-shadow: 0 3px 8px rgba(0,0,0,.55);
  }
  .card-front { left: 302px; top: 129px; background: var(--card-white); }
  .card-back {
    left: 299px; top: 488px; overflow: hidden;
    background: linear-gradient(180deg, #7eabe8 0%, #4d89d6 40%, #1c5fb5 75%, var(--brand-blue) 100%);
  }

  .brand-block { position: absolute; left: 40px; top: 30px; width: 260px; }
  .wordmark {
    display: flex; align-items: center; gap: 8px;
    font-family: "Questrial", sans-serif; font-size: 44px; line-height: 1;
    color: var(--brand-blue); letter-spacing: -0.5px;
  }
  .wordmark-dot { width: 12px; height: 12px; border-radius: 50%; background: var(--brand-blue); }
  .brand-motto {
    margin-top: 12px; padding-left: 58px;
    font-family: "Roboto", sans-serif; font-weight: 500; font-size: 13.5px;
    color: var(--ink); letter-spacing: .2px;
  }
  .brand-promise {
    margin-top: 2px; padding-left: 12px;
    font-family: "Roboto", sans-serif; font-style: italic; font-size: 14px;
    color: var(--ink-soft);
  }

  .contact { position: absolute; right: 31px; top: 150px; text-align: right; }
  .contact-name {
    font-family: "Roboto", sans-serif; font-weight: 700; font-size: 22px;
    color: var(--brand-blue); line-height: 1.1; margin-bottom: 4px;
  }
  .contact-group {
    font-family: "Didact Gothic", sans-serif; font-size: 14.5px; line-height: 18px;
    color: var(--ink-muted);
  }
  .contact-group.primary { color: var(--ink); }
  .contact-group + .contact-group { margin-top: 8px; }

  .world-map {
    position: absolute; inset: 0;
    background: radial-gradient(ellipse 70% 45% at 50% 30%, rgba(207,222,237,.22), rgba(207,222,237,0) 70%);
  }
  .back-wordmark {
    position: absolute; left: 0; right: 0; top: 148px;
    display: flex; justify-content: center; align-items: center; gap: 12px;
    font-family: "Questrial", sans-serif; font-size: 64px; line-height: 1;
    color: var(--card-white);
  }
  .back-wordmark .wordmark-dot { width: 16px; height: 16px; background: var(--card-white); }
  .back-tagline {
    position: absolute; left: 0; right: 0; top: 286px; text-align: center;
    font-family: "Roboto", sans-serif; font-style: italic; font-weight: 700; font-size: 15px;
    color: var(--card-white);
  }
</style>
</head>
<body>
<main class="canvas">
  <section class="card card-front">
    <div class="brand-block">
      <div class="wordmark"><span class="wordmark-dot"></span>Halvor Pinet</div>
      <p class="brand-motto">YOUR EYE IN THE SKY</p>
      <p class="brand-promise">Watch &amp; Monitor on the Web 24/7</p>
    </div>
    <div class="contact">
      <h1 class="contact-name">CORIN ASHDALE</h1>
      <p class="contact-group primary">cashdale@halvorpinet.com.au<br>0400 555 172</p>
      <p class="contact-group">Tel: +61 3 9555 0142<br>Fax: +61 3 9555 0143<br>www.halvorpinet.com.au</p>
      <p class="contact-group">Halvor Pinet Rentals Pty Ltd/ABN: 00 000 000 000<br>4,18 Kestrel Street, Marlow VIC 3999</p>
    </div>
  </section>

  <section class="card card-back">
    <div class="world-map" role="img" aria-label="Faint world map in pale blue across the card"></div>
    <div class="back-wordmark"><span class="wordmark-dot"></span>Halvor Pinet</div>
    <p class="back-tagline">Premium Suppliers of Real Time Temperature Tracking</p>
  </section>
</main>
</body>
</html>
```